Company raising consciousness thru leadership & self-awareness needs amazing Letterhead

We are a technology company that spun out of a consulting firm. We are waking people up in corporate America through surveys, leadership development, workshops and consulting. Getting employees to become self-aware and changing company culture through improved leadership and team effectiveness. We need Word letterhead for our proposals, handouts, and worksheets that match our brand standard, is fresh, and communicates trust, credibility and professionalism.

Target Market(s)

Our target clients are other businesses, and executive leaders and C-suite leaders in those companies.

Font styles to use
Sans Serif

Requirements
Must have
• A Word template we can use for handouts, proposals, executive summary, project management documents, and letters. We need our logo. Please add page number and date on the footer. Must match the theme of our new website in look and feel to match the brand we are trying to promote. Use the colors from our brand standard document I submitted.

```html
<!DOCTYPE html>
<html lang="en">
<head>
<meta charset="utf-8">
<title>Lumen Aware Partners — Letterhead</title>
<link rel="stylesheet" href="https://fonts.googleapis.com/css2?family=Montserrat:wght@400;500;700&display=swap">
<style>
  :root {
    --bg: #d6d6d8;
    --paper: #ffffff;
    --navy: #25346a;
    --purple: #7d3f98;
    --wash: #dfe8f2;
    --wash-soft: rgba(223, 232, 242, 0);
  }
  * { box-sizing: border-box; margin: 0; padding: 0; }
  html, body {
    width: 1200px;
    height: 1200px;
    overflow: hidden;
    background: var(--bg);
    font-family: "Montserrat", sans-serif;
  }
  .sheet {
    position: absolute;
    left: 200px;
    top: 34px;
    width: 800px;
    height: 1131px;
    background: var(--paper);
    box-shadow: 0 6px 24px rgba(0, 0, 0, 0.18);
    overflow: hidden;
  }
  .brand {
    position: absolute;
    left: 44px;
    top: 40px;
    display: flex;
    align-items: center;
    gap: 14px;
  }
  .brand-dot {
    width: 64px;
    height: 64px;
    border-radius: 50%;
    background: var(--navy);
  }
  .brand-name {
    font-size: 17px;
    font-weight: 700;
    color: var(--navy);
    line-height: 1.25;
    letter-spacing: 0.04em;
    text-transform: uppercase;
  }
  .header-wash {
    position: absolute;
    right: 0;
    top: 90px;
    width: 360px;
    height: 230px;
    background: radial-gradient(ellipse at 60% 45%, var(--wash) 0%, var(--wash) 40%, var(--wash-soft) 75%);
  }
  .contact {
    position: absolute;
    right: 52px;
    top: 170px;
    text-align: right;
    font-size: 15px;
    line-height: 1.45;
    color: var(--navy);
    font-style: normal;
  }
  .contact .accent {
    color: var(--purple);
    font-weight: 700;
  }
  .footer-band {
    position: absolute;
    left: 0;
    top: 985px;
    width: 560px;
    height: 80px;
  }
  .footer-meta {
    position: absolute;
    right: 52px;
    bottom: 36px;
    font-size: 17px;
    color: var(--navy);
    letter-spacing: 0.02em;
  }
  .footer-meta .label {
    color: var(--purple);
    font-weight: 700;
  }
  .footer-meta .item + .item { margin-left: 22px; }
</style>
</head>
<body>
  <main class="sheet">
    <div class="brand">
      <span class="brand-dot"></span>
      <span class="brand-name">Lumen Aware<br>Partners</span>
    </div>

    <div class="header-wash" role="img" aria-label="Soft pale blue watercolour wash behind the contact details"></div>

    <address class="contact">
      1740 Harbor Lane, Suite #204<br>
      Orlando, FL 32811<br>
      <span class="accent">123-555-0147</span><br>
      <span class="accent">lumenaware.com</span>
    </address>

    <svg class="footer-band" viewBox="0 0 560 80" aria-hidden="true">
      <path d="M0 0 L330 22 L420 28 L470 30 L520 33 L560 36 L500 44 L430 56 L360 68 L300 80 L0 80 Z" fill="var(--purple)"/>
    </svg>

    <footer class="footer-meta">
      <span class="item"><span class="label">DATE:</span> 20-12-2020</span>
      <span class="item"><span class="label">PG NO:</span> 01</span>
    </footer>
  </main>
</body>
</html>
```